Need a business card for our overland brand!

We had the logo made and we need a great design for our business card. Use the logo provide or tweak it however you see fit.

Contact Information for Business Card

Name, Title, Telephone, email, website

```html
<!DOCTYPE html>
<html lang="en">
<head>
<meta charset="utf-8">
<title>Northridge Trails — Business Card</title>
<link rel="stylesheet" href="https://fonts.googleapis.com/css2?family=Montserrat:wght@300;400;600;800&display=swap">
<style>
  :root {
    --stage: #2a2d32;
    --navy: #0a2a4a;
    --navy-band: #173b55;
    --ink: #0f2a48;
    --cyan: #1fa3c9;
    --white: #ffffff;
    --muted: #2c3e55;
  }
  * { box-sizing: border-box; margin: 0; padding: 0; }
  html, body { width: 1200px; height: 780px; overflow: hidden; }
  body {
    background: var(--stage);
    font-family: "Montserrat", sans-serif;
    position: relative;
  }
  .card {
    position: absolute;
    width: 500px;
    height: 286px;
    border-radius: 16px;
    overflow: hidden;
    top: 247px;
  }

  /* Back side */
  .card--back { left: 50px; background: var(--navy); }
  .card--back .band {
    position: absolute; left: 0; right: 0; top: 66px; height: 120px;
    background: var(--navy-band);
  }
  .card--back .rule {
    position: absolute; top: 108px; height: 2px; background: var(--cyan);
  }
  .card--back .rule--left { left: 0; width: 120px; }
  .card--back .rule--right { right: 0; width: 120px; top: 136px; }
  .card--back .brand {
    position: absolute; left: 0; right: 0; top: 92px;
    text-align: center; color: var(--white);
    font-weight: 800; font-size: 26px; line-height: 30px; letter-spacing: 1px;
    text-transform: uppercase;
  }
  .card--back .site {
    position: absolute; left: 0; right: 0; bottom: 30px;
    display: flex; align-items: center; justify-content: center; gap: 8px;
    color: var(--white); font-weight: 400; font-size: 12px; letter-spacing: .5px;
  }

  /* Front side */
  .card--front { left: 650px; background: var(--white); }
  .card--front .name {
    position: absolute; left: 40px; top: 30px;
    color: var(--ink); font-size: 26px; line-height: 30px;
  }
  .name .first { font-weight: 600; }
  .name .last { font-weight: 300; }
  .card--front .title {
    position: absolute; left: 36px; top: 62px;
    color: var(--ink); font-weight: 400; font-size: 11px; letter-spacing: 5px;
  }
  .card--front .divider {
    position: absolute; left: 0; width: 430px; top: 88px; height: 1.5px;
    background: var(--cyan);
  }
  .contacts {
    position: absolute; left: 24px; top: 112px;
    list-style: none; display: flex; flex-direction: column; gap: 12px;
  }
  .contacts li {
    display: flex; align-items: center; gap: 14px;
    color: var(--muted); font-size: 10.5px; font-weight: 400;
  }
  .contacts .icon {
    width: 24px; height: 24px; border-radius: 50%;
    background: var(--ink);
    display: flex; align-items: center; justify-content: center;
  }
  .card--front .brand {
    position: absolute; right: 30px; top: 128px; text-align: right;
    color: var(--ink); font-weight: 800; font-size: 24px; line-height: 27px;
    text-transform: uppercase; letter-spacing: 1px;
  }
</style>
</head>
<body>

  <section class="card card--back" aria-label="Card back">
    <div class="band"></div>
    <div class="rule rule--left"></div>
    <div class="rule rule--right"></div>
    <div class="brand">Northridge<br>Trails</div>
    <div class="site">
      <svg width="12" height="12" viewBox="0 0 12 12" fill="none" stroke="#fff" stroke-width="1">
        <circle cx="6" cy="6" r="5"/><ellipse cx="6" cy="6" rx="2.2" ry="5"/><line x1="1" y1="6" x2="11" y2="6"/>
      </svg>
      <span>www.northridgetrails.com</span>
    </div>
  </section>

  <section class="card card--front" aria-label="Card front">
    <h1 class="name"><span class="first">Martin</span> <span class="last">Hale</span></h1>
    <p class="title">Design</p>
    <div class="divider"></div>
    <ul class="contacts">
      <li>
        <span class="icon">
          <svg width="12" height="12" viewBox="0 0 12 12" fill="#fff">
            <path d="M3 1.5l1.6 2.3-1 1c.6 1.3 1.6 2.3 2.9 2.9l1-1 2.3 1.6-.8 1.9C5 10 2 7 1.7 2.3z"/>
          </svg>
        </span>
        <span>+18 2555 0142 3307</span>
      </li>
      <li>
        <span class="icon">
          <svg width="12" height="12" viewBox="0 0 12 12" fill="#fff">
            <path d="M1 6l10-4.5L8 11 6 7z"/>
          </svg>
        </span>
        <span>hello@northridgetrails.com</span>
      </li>
      <li>
        <span class="icon">
          <svg width="12" height="12" viewBox="0 0 12 12" fill="none" stroke="#fff" stroke-width="1">
            <circle cx="6" cy="6" r="5"/><ellipse cx="6" cy="6" rx="2.2" ry="5"/><line x1="1" y1="6" x2="11" y2="6"/>
          </svg>
        </span>
        <span>www.northridgetrails.com</span>
      </li>
    </ul>
    <div class="brand">Northridge<br>Trails</div>
  </section>

</body>
</html>
```